Young, modern, highly skilled carpenter needs business card design

I need a business card design for my construction business. Its called 'Pemberton Building Partners'. Im looking for a ultra modern design that incorporates P B P, the first letters of the name with only a subtle reference to carpentry. The design should reflect my high quality work and eye for detail. i have also uploaded some exmaple designs i like.

Industry/Entity Type

Construction

Requirements
Must have
• Name of business, my name, mobile number, ABN number, email address
Nice to have
• A logo incorporating the name of the business

```html
<!DOCTYPE html>
<html lang="en">
<head>
<meta charset="utf-8">
<title>Pemberton Building Partners – Business Card</title>
<link rel="stylesheet" href="https://fonts.googleapis.com/css2?family=Tinos:wght@400&display=swap">
<style>
  :root {
    --frame: #050505;
    --wood-light: #9c968c;
    --wood-mid: #7d776e;
    --wood-dark: #4e4a44;
    --panel: #050505;
    --type-grey: #8f8f8f;
    --rule-grey: #3a3a3a;
  }
  html, body {
    margin: 0;
    padding: 0;
    width: 1200px;
    height: 725px;
    overflow: hidden;
    background: var(--frame);
  }
  .business-card {
    position: relative;
    width: 1200px;
    height: 725px;
    box-sizing: border-box;
    border: 12px solid var(--frame);
    overflow: hidden;
  }
  .wood-backdrop {
    position: absolute;
    inset: 0;
    background:
      linear-gradient(90deg,
        var(--wood-mid) 0%, var(--wood-light) 10%, var(--wood-mid) 19%,
        var(--wood-dark) 20%, var(--wood-light) 23%, var(--wood-mid) 38%,
        var(--wood-dark) 44%, var(--wood-light) 48%, var(--wood-mid) 60%,
        var(--wood-light) 70%, var(--wood-dark) 74%, var(--wood-mid) 78%,
        var(--wood-light) 88%, var(--wood-mid) 100%);
  }
  .identity-panel {
    position: absolute;
    left: 372px;
    top: 150px;
    width: 761px;
    height: 330px;
    box-sizing: border-box;
    padding: 26px 40px 0;
    background: var(--panel);
    font-family: "Tinos", "Times New Roman", serif;
    font-weight: 400;
    color: var(--type-grey);
    text-align: center;
  }
  .business-monogram {
    margin: 0;
    font-size: 96px;
    font-weight: 400;
    letter-spacing: 0.12em;
    line-height: 1;
  }
  .business-name {
    margin: 14px 0 0;
    font-size: 36px;
    line-height: 1;
  }
  .contact-rule {
    width: 560px;
    height: 1px;
    margin: 28px auto 22px;
    background: var(--rule-grey);
  }
  .contact-details {
    display: grid;
    grid-template-columns: 1fr 1fr;
    row-gap: 12px;
    column-gap: 30px;
    margin: 0;
    padding: 0;
    list-style: none;
    font-size: 22px;
    line-height: 1.2;
  }
  .contact-owner { text-align: right; }
  .contact-mobile { text-align: left; }
  .contact-abn { text-align: right; }
  .contact-email { text-align: left; }
</style>
</head>
<body>
  <main class="business-card">
    <div class="wood-backdrop" role="img" aria-label="Weathered grey wooden planks with vertical grain"></div>
    <section class="identity-panel">
      <h1 class="business-monogram">P B P</h1>
      <p class="business-name">Pemberton Building Partners</p>
      <div class="contact-rule"></div>
      <ul class="contact-details">
        <li class="contact-owner">Liam Pemberton</li>
        <li class="contact-mobile">Mobile 0412 345 678</li>
        <li class="contact-abn">ABN 12 345 678 901</li>
        <li class="contact-email">liam@pembertonbp.com.au</li>
      </ul>
    </section>
  </main>
</body>
</html>
```